Tax Preparation flyer for LedgerWise Corp.

My Client would like a one page PDF flyer to promote upcoming tax season in Canada. This firm is affordable and all virtual. I have attached a copy of their logo and a word document with the proposed wording for the flyer. Please feel free to change if you have better suggestions.

Target Market(s)

individuals in canada

Colors
0054AA
0677BA
7BADD7
CADEEF
E8F1F8

```html
<!DOCTYPE html>
<html lang="en">
<head>
<meta charset="utf-8">
<title>LedgerWise Corp. – Tax Season Flyer</title>
<link rel="stylesheet" href="https://fonts.googleapis.com/css2?family=Poppins:wght@400;500;600;700;800;900&display=swap">
<style>
  :root{
    --navy:#0054AA;
    --blue:#0677BA;
    --sky:#2A9AD8;
    --light:#7BADD7;
    --pale:#CADEEF;
    --mist:#E8F1F8;
    --red:#E8262A;
    --ink:#2B2D31;
    --dark:#1F2A33;
    --dark-2:#24343F;
    --white:#FFFFFF;
    --page-bg:#B9BCBF;
    --team-square:#5B5FC7;
  }
  *{box-sizing:border-box;margin:0;padding:0}
  html,body{width:1200px;height:2486px;overflow:hidden}
  body{background:var(--page-bg);font-family:"Poppins",sans-serif;position:relative}

  .flyer{position:absolute;left:91px;top:523px;width:1018px;height:1440px;overflow:hidden;
    background:linear-gradient(to bottom,var(--white) 0,var(--white) 505px,var(--dark) 505px,var(--dark-2) 1000px,var(--dark) 1440px);
    box-shadow:0 20px 40px rgba(0,0,0,.35)}
  .abs{position:absolute}

  .brand{left:48px;top:62px;display:flex;align-items:center;gap:12px;font-weight:700;font-size:38px;color:var(--ink);letter-spacing:-.5px}
  .brand-dot{width:22px;height:22px;border-radius:50%;background:var(--sky)}

  .headline{left:46px;top:160px;font-weight:900;line-height:1}
  .headline .relax{display:block;color:var(--red);font-size:86px;letter-spacing:1px}
  .headline .got{display:block;color:var(--ink);font-size:43px;margin-top:8px;font-weight:800}
  .headline .taxes{display:block;color:var(--blue);font-size:76px;margin-top:8px;letter-spacing:1px}
  .headline .covered{display:block;color:var(--blue);font-size:76px;margin-top:4px;letter-spacing:1px}

  .hero-art{left:475px;top:0;width:543px;height:465px;
    background:radial-gradient(ellipse at 55% 60%,#F4E3D3 0,#F6ECE4 35%,rgba(255,255,255,0) 70%),
               linear-gradient(120deg,#FFFFFF 0,#F9D6D0 50%,#E8262A 100%);opacity:.85;border-radius:4px}

  .intro-bar{left:52px;top:467px;width:915px;height:113px;background:var(--sky);border-radius:4px}
  .intro-bar p{position:absolute;left:200px;top:14px;width:700px;color:var(--white);font-size:16.5px;line-height:21px}
  .badge{left:55px;top:460px;width:178px;height:107px;background:var(--red);border-radius:4px;color:var(--white);text-align:center;font-weight:600;box-shadow:3px 4px 0 rgba(0,0,0,.2)}
  .badge .small{display:block;font-size:13px;line-height:15px;margin-top:10px}
  .badge .big{display:block;font-size:26px;font-weight:800;line-height:27px;margin-top:6px}

  .portal-copy{left:48px;top:612px;width:440px;color:var(--white);font-size:14.5px;line-height:17px}
  .meet-line{left:48px;top:686px;width:440px;color:var(--sky);font-weight:600;font-size:12.5px;line-height:17px}
  .meet-line .meet-name{display:inline-block;font-size:19px;font-weight:700;line-height:17px;margin-left:8px;vertical-align:-2px}
  .meet-line .sq{display:inline-block;width:18px;height:18px;background:var(--team-square);border-radius:3px;margin-left:12px;vertical-align:-4px}

  .pricing-tab{left:48px;top:738px;height:42px;width:170px;background:var(--sky);border-radius:0 22px 22px 0;color:var(--white);font-weight:800;font-size:30px;line-height:42px;padding-left:14px;border-left:4px solid var(--white)}
  .personal{left:48px;top:792px;color:var(--white);font-size:30px;line-height:30px}
  .personal .sub{display:block;color:var(--sky);font-weight:700;font-size:24px;line-height:26px}
  .price-main{left:218px;top:780px;color:var(--white);font-weight:800;font-size:70px;line-height:80px}
  .price-main sup,.price-add sup{font-size:.5em;vertical-align:top;line-height:1.6}
  .divider{left:48px;top:871px;width:425px;border-top:1px dashed var(--light)}

  .add-title{left:48px;top:884px;color:var(--white);font-size:22px;line-height:30px}
  .price-add{left:48px;top:922px;color:var(--white);font-weight:800;font-size:46px;line-height:50px}
  .add-label{left:164px;top:929px;color:var(--white);font-size:18px;line-height:21px}
  .add-label span{color:var(--sky);font-weight:700;display:block}

  .notes{left:48px;top:987px;width:440px;list-style:none;color:var(--white);font-size:14px;line-height:16.5px}
  .notes li{position:relative;padding-left:18px;margin-bottom:8px}
  .notes li svg{position:absolute;left:0;top:3px}
  .breathe{left:48px;top:1166px;color:var(--white);font-size:19px;line-height:26px}
  .breathe b{color:var(--sky);font-weight:700}

  .workflow-art{left:545px;top:605px;width:395px;height:285px;border-radius:6px;
    background:radial-gradient(ellipse at 50% 55%,#E9EEF2 0,#9FB3C2 40%,rgba(36,52,63,0) 72%)}
  .autopilot{left:545px;top:903px;width:425px;color:var(--white);font-size:14px;line-height:16.5px}

  .feel-box{left:560px;top:998px;width:407px;height:185px;background:var(--sky);border-radius:0 8px 8px 0}
  .feel-box .copy{position:absolute;left:107px;top:14px;width:290px;color:var(--white);font-size:14px;line-height:16.5px}
  .feel-box .q{color:var(--red);font-weight:600;display:block}
  .feel-box .copy p{margin-bottom:10px}
  .question-art{left:538px;top:998px;width:125px;height:188px;border-radius:50% 50% 10px 10px;
    background:linear-gradient(180deg,var(--red) 0,#C61D21 100%)}

  .costs{left:48px;top:1211px;width:920px;height:126px;background:var(--white);border:3px solid var(--sky);border-radius:8px;overflow:hidden}
  .costs .title{height:30px;background:var(--sky);color:var(--white);text-align:center;font-weight:700;font-size:17px;line-height:30px}
  .costs table{width:100%;border-collapse:collapse;table-layout:fixed;text-align:center}
  .costs th{background:var(--pale);color:var(--ink);font-weight:700;font-size:13.5px;line-height:15px;height:42px;border-right:2px solid var(--white)}
  .costs td{color:var(--ink);font-size:13px;line-height:16px;height:48px;vertical-align:top;padding-top:8px;border-right:1px solid var(--pale)}
  .costs th:last-child,.costs td:last-child{border-right:none}
  .costs sup{font-size:8px}

  .contact{left:48px;top:1358px;width:922px;display:flex;align-items:center;justify-content:space-between;color:var(--white);font-size:21px;font-weight:600}
  .contact .call{font-weight:800;font-size:27px}
  .contact .call b{color:var(--sky)}
  .contact .item{display:flex;align-items:center;gap:8px}
</style>
</head>
<body>
<main class="flyer">

  <div class="abs brand"><span class="brand-dot"></span>LedgerWise Corp.</div>

  <h1 class="abs headline">
    <span class="relax">RELAX</span>
    <span class="got">WE’VE GOT YOUR</span>
    <span class="taxes">TAXES</span>
    <span class="covered">COVERED!</span>
  </h1>

  <div class="abs hero-art" role="img" aria-label="Red and white map of Canada with a payment terminal labelled TAX and banknotes falling from above"></div>

  <section class="abs intro-bar">
    <p>We worked both in public accounting firms as well as specialized tax.  Our tax services are virtual, so you don’t have to take the time for a personal visit. We take care of everything and can access all your tax slips from CRA website directly into our tax software. All signing is done via SignFlow</p>
  </section>
  <div class="abs badge">
    <span class="small">OUR TAX PREPARERS<br>HAVE OVER</span>
    <span class="big">20 YEARS<br>EXPERIENCE</span>
  </div>

  <p class="abs portal-copy">You can fill and submit the appropriate forms, along with all your other documents, in our secure client portal. It’s important that we understand your situation and any changes in your situation from the past year.</p>
  <p class="abs meet-line">If you have a complex tax situation and would like to<br>discuss it, we can meet in virtually over<span class="meet-name">MeetLine</span><span class="sq"></span></p>

  <div class="abs pricing-tab">PRICING</div>
  <p class="abs personal">PERSONAL<span class="sub">TAX RETURN</span></p>
  <p class="abs price-main"><sup>$</sup>100.00</p>
  <div class="abs divider"></div>

  <p class="abs add-title">Add a business or rental schedule</p>
  <p class="abs price-add"><sup>$</sup>125</p>
  <p class="abs add-label">PER BUSINESS OR<span>RENTAL PROPERTY</span></p>

  <ul class="abs notes">
    <li><svg width="11" height="11" viewBox="0 0 11 11"><circle cx="5.5" cy="5.5" r="5.5" fill="#2A9AD8"/><path d="M3 5.6l1.7 1.7L8 4" stroke="#fff" stroke-width="1.5" fill="none"/></svg>More complex tax returns will be assessed based on the complexity of the return and you will be advised before we start.</li>
    <li><svg width="11" height="11" viewBox="0 0 11 11"><circle cx="5.5" cy="5.5" r="5.5" fill="#2A9AD8"/><path d="M3 5.6l1.7 1.7L8 4" stroke="#fff" stroke-width="1.5" fill="none"/></svg>Did you fall behind in filing your income tax save 20% when you file 3 or more years with us.  We can do back to 2012 for filing of tax returns.</li>
    <li><svg width="11" height="11" viewBox="0 0 11 11"><circle cx="5.5" cy="5.5" r="5.5" fill="#2A9AD8"/><path d="M3 5.6l1.7 1.7L8 4" stroke="#fff" stroke-width="1.5" fill="none"/></svg>If you expect a refund, the earlier you file the sooner you will receive your refund.  Our average turn around time prior to April is a couple of days.</li>
  </ul>
  <p class="abs breathe">TODAY SO YOU CAN START TO <b>BREATHE EASY</b></p>

  <div class="abs workflow-art" role="img" aria-label="Isometric illustration of a laptop printing receipts, a phone, business people exchanging documents and finance icons"></div>
  <p class="abs autopilot">Imagine having your bookkeeping on auto pilot, with everything always up to date and available at your fingertips. Anytime. Anywhere. You’ll always know exactly where you stand with your cash flow—how much you have, owe, are owed, and have made.</p>

  <section class="abs feel-box">
    <div class="copy">
      <p><span class="q">How will you feel?</span>Calm, relaxed, and able to make good business decisions. And you’ll have more time to work on your business. In short, you’ll be able to breathe easy.</p>
      <p><span class="q">Sound too good to be true?</span>That’s exactly how our clients feel once all their bookkeeping stresses are gone.</p>
    </div>
  </section>
  <div class="abs question-art" role="img" aria-label="Large red question mark with a businessman sitting against it"></div>

  <section class="abs costs">
    <div class="title">BOOKKEEPING &amp; ACCOUNTING COSTS</div>
    <table>
      <tr><th>DIY</th><th>PART-TIME<br>BOOKKEEPER</th><th>FULL-TIME<br>BOOKKEEPER</th><th>FULL OUTSOURCED<br>ACCOUNTING TEAM</th></tr>
      <tr><td>No added financial cost</td><td>$3,500-4,500/ month<br>+ benefits<sup>(1)</sup></td><td>$4,800-5,500/ month<br>+ benefits <sup>(2)</sup></td><td>$5,000+<sup>(3)</sup></td></tr>
    </table>
  </section>

  <footer class="abs contact">
    <span class="call">CALL US <b>TODAY</b></span>
    <span class="item"><svg width="20" height="20" viewBox="0 0 20 20"><circle cx="10" cy="10" r="9" fill="none" stroke="#2A9AD8" stroke-width="2"/><path d="M7 5.5c-1 1-1 3 1 5.5s4.5 3 5.5 2l-1.5-2-1.5.7c-1-.5-2-1.6-2.6-2.6l.7-1.5z" fill="#2A9AD8"/></svg>555 210 4477</span>
    <span class="item"><svg width="20" height="15" viewBox="0 0 20 15"><rect x="1" y="1" width="18" height="13" fill="none" stroke="#2A9AD8" stroke-width="2"/><path d="M1 1l9 7 9-7" fill="none" stroke="#2A9AD8" stroke-width="2"/></svg>info@ledgerwise.com</span>
    <span class="item"><svg width="18" height="18" viewBox="0 0 18 18"><circle cx="9" cy="9" r="8" fill="none" stroke="#2A9AD8" stroke-width="1.8"/><ellipse cx="9" cy="9" rx="3.5" ry="8" fill="none" stroke="#2A9AD8" stroke-width="1.5"/><path d="M1 9h16" stroke="#2A9AD8" stroke-width="1.5"/></svg>www.ledgerwise.com</span>
  </footer>

</main>
</body>
</html>
```